Stationery for use with Ninefold Ridge reports

I would like to get a stationery design that my firm -- Ninefold Ridge Advisory -- will use as a format for reports that we send our clients. I am specifically looking for a design for use on a piece of paper or letterhead -- not business cards or envelopes.

We are an Africa based US risk intelligence and strategy firm that works with multinational corporations operating in West Africa. Our initial thinking is that we would like a color scheme consistent with our existing logo -- however we are open to other color schemes.

Also, we would like to see at least two separate versions: one with our company name and logo, the other without name and logo.

We also would like font recommendations for the stationary design.

The final design should communicate discreet professionalism and a modern approach, but it should not overshadow the words and information printed on the stationery.

Target Market(s)

Multinational corporations that currently use our products.

Font styles to use
Serif
Sans Serif

Requirements
Must have
• Sense of discreet professionalism that will not overshadow the content we put onto the stationery format.
• We would like to see designs with and without our company name/logo.
• Please suggest fonts that would work with the stationery.
Nice to have
• Ideally colors consistent with out existing logo, though we are open to and even encourage other ideas.
Should not have
• No need for business cards or envelopes.

```html
<!DOCTYPE html>
<html lang="en">
<head>
<meta charset="utf-8">
<title>Ninefold Ridge Letterhead</title>
<link rel="stylesheet" href="https://fonts.googleapis.com/css2?family=Noto+Sans:wght@400;600&display=swap">
<style>
  :root {
    --backdrop: #e4e4e4;
    --paper: #ffffff;
    --ink: #5a5a5a;
    --rule: #1e2a36;
    --brand-gold: #e0a548;
    --brand-sky: #a9d4ee;
    --brand-dark: #1e2a36;
  }
  * { margin: 0; padding: 0; box-sizing: border-box; }
  html, body {
    width: 1200px; height: 960px; overflow: hidden;
    background: var(--backdrop);
    font-family: "Noto Sans", sans-serif;
  }
  .letterhead {
    position: absolute; left: 284px; top: 30px;
    width: 631px; height: 900px;
    background: var(--paper);
    box-shadow: 0 2px 10px rgba(0,0,0,0.12);
    overflow: hidden;
  }
  .brand {
    position: absolute; left: 33px; top: 48px;
    display: flex; align-items: center; gap: 8px;
  }
  .brand-mark {
    width: 14px; height: 14px; background: var(--brand-gold);
  }
  .brand-name {
    font-size: 17px; font-weight: 600; color: var(--brand-dark);
    letter-spacing: 0.3px;
  }
  .header-rule {
    position: absolute; left: 33px; top: 116px;
    width: 565px; height: 2px; background: var(--rule);
  }
  .letter-date {
    position: absolute; left: 62px; top: 266px;
    font-size: 11px; color: var(--ink);
  }
  .letter-body {
    position: absolute; left: 62px; top: 320px; width: 520px;
    font-size: 11px; color: var(--ink); line-height: 23px;
  }
  .letter-body p { margin-bottom: 3px; }
  .letter-body p + p { margin-top: 0; }
  .letter-body .line { display: block; white-space: nowrap; }
  .signoff {
    position: absolute; left: 441px; top: 628px;
    font-size: 10.5px; color: var(--ink); line-height: 13px;
  }
  .signature {
    display: block; width: 128px; height: 40px; margin-bottom: 4px;
    background: linear-gradient(90deg, rgba(120,120,120,0.05), rgba(120,120,120,0.18), rgba(120,120,120,0.05));
    border-radius: 4px;
  }
  .signoff-name { display: block; margin-left: 2px; }
  .footer-band {
    position: absolute; left: 0; bottom: 0; width: 631px; height: 17px;
  }
</style>
</head>
<body>
  <main class="letterhead">
    <header class="brand">
      <span class="brand-mark"></span>
      <span class="brand-name">Ninefold Ridge</span>
    </header>
    <div class="header-rule"></div>

    <p class="letter-date">Date, 10 September, 2020</p>

    <section class="letter-body">
      <p>
        <span class="line">This is a sample letter that has been placed to demonstrate typing remat (Your Company). letterhead</span>
        <span class="line">design. When positioned properly, it will serve to work in harmony with all other elements letterhead.</span>
        <span class="line">This letterhead design is meant to project an image</span>
      </p>
      <p>
        <span class="line">This letterhead design is meant project an image of professionalism reliability. By using simple aligen</span>
        <span class="line">we have created a very spacious feeling. The simplicity suggest &nbsp;rengththe spaciousnes contributes h</span>
        <span class="line">aesthetics the layout. These basic qualities along with the (Your Company)</span>
      </p>
      <p>
        <span class="line">look and helps reinforce the (Your Company) brand. letterhead design is meant to project an image p</span>
        <span class="line">design. When positioned properly, it will serve to work in harmony all the other elements letterhead.</span>
        <span class="line">sionalism and reliability.</span>
      </p>
      <p>
        <span class="line">This letterhead design is based on the (Form of your logo) form (Your Company) logo. Each stationery</span>
        <span class="line">we have created a very spacious feeling. The simplicity suggests strength the spaciousnes contribute</span>
        <span class="line">part of the (Form of your logo).</span>
      </p>
    </section>

    <div class="signoff">
      <span class="signature" role="img" aria-label="Handwritten signature of Marcus Adeyemi"></span>
      <span class="signoff-name">Marcus Adeyemi</span>
      <span class="signoff-name">Manager</span>
    </div>

    <svg class="footer-band" viewBox="0 0 631 17" width="631" height="17" aria-hidden="true">
      <polygon points="0,0 518,0 508,17 0,17" fill="var(--brand-gold)"/>
      <polygon points="527,0 631,0 631,17 517,17" fill="var(--brand-sky)"/>
    </svg>
  </main>
</body>
</html>
```